Home page for local retail aggregator

About us: We are a new company that showcases beautiful products available at nearby retail stores. This homepage is meant to display the latest products featured on our site and also allow the user to search, browse with filters, and access their account details.

Currently, our home page looks a little bland. We want the focus of the site to remain on the featured photos and products but the design should be more cohesive. The most successful designs will make more subtle use of our colors, provide intuitive menu controls, and look visually stunning.

This homepage has a few sections:

Header:
-Top Section: will always remain at the top of the page. There should be space for our company name ”zAntelope”, a tagline, and a place for the menus.
-Menus: user must be able to find links for: “My profile” “My Products” “Add Product” “Preview store”
-Bottom section: this will scroll with the user and always remain at the top of the screen providing access to a search box, and filters for “location” “price” and retail categories.

Main Page:
-Each product featured is shown on a tile that includes a photo, title, price, name of store, has space to leave a comment, and include counters for "likes," comments, and "Pods"). “Pods” are bookmark folders. The user’s profile pic is also shown in miniature if they leave a comment.

The final version of the site must be delivered in a fully layered photoshop file and have versions demonstrating what the page will look like both when a user is logged-in and when logged-out.

Target Market(s)

Most of our users are female 18-45. Our customers are retail store owners who want their products to look attractive and professional.

Industry/Entity Type

Retail

Requirements
Must have
• Our logo must be present on the site (attached to project). You're welcome to change the colors in the header but it should look good with our logo.

For reference here are colors we're currently using:
Site text is in Dark Blue: RGB(10/23/47)
Logo color on business cards is light blue: (51/153/204)
Nice to have
• Would love to see new versions of the menus that are more modern and intuitive. Currently we just have links to each individual control. Putting these in a drop-down or re-arranging them would be nice.

```html
<!DOCTYPE html>
<html lang="en">
<head>
<meta charset="utf-8">
<title>zAntelope – Local Product Search &amp; Discovery</title>
<link href="https://fonts.googleapis.com/css2?family=Open+Sans:wght@400;600;700&display=swap" rel="stylesheet">
<style>
:root{
  --header-blue:#234b8e;
  --header-blue-dark:#1c3f7a;
  --tagline-blue:#9cc9f0;
  --link-blue:#3a8fd6;
  --text-dark:#0a172f;
  --text-body:#4a4f57;
  --nav-bg:#f2f2f2;
  --page-bg:#e4e4e4;
  --card-bg:#ffffff;
  --band-bg:#f3f3f3;
  --line:#e2e2e2;
  --bar-bg:#d9d9d9;
  --placeholder:#c5c5c5;
}
*{box-sizing:border-box;margin:0;padding:0}
html,body{width:1200px;height:900px;overflow:hidden}
body{font-family:"Open Sans",Arial,sans-serif;background:var(--page-bg);color:var(--text-dark);position:relative}

/* header */
.site-header{position:absolute;left:0;top:0;width:1200px;height:68px;background:linear-gradient(var(--header-blue),var(--header-blue-dark))}
.brand-mascot{position:absolute;left:208px;top:15px;width:74px;height:83px;border-radius:40px 40px 18px 18px;background:linear-gradient(#5fb3ea,#2f86c8);z-index:3}
.brand-name{position:absolute;left:287px;top:22px;font-size:37px;font-weight:700;color:#fff;line-height:1}
.tagline{position:absolute;left:499px;top:38px;font-size:14px;font-weight:700;color:var(--tagline-blue);letter-spacing:.3px}
.social{position:absolute;top:36px;width:24px;height:24px;border-radius:50%;background:#3a8fd6}
.main-nav{position:absolute;left:0;top:68px;width:1200px;height:46px;background:var(--nav-bg);border-bottom:1px solid #dcdcdc}
.nav-link{position:absolute;top:16px;font-size:11px;color:#5a5a5a;text-transform:uppercase;display:flex;align-items:center;gap:7px;white-space:nowrap}
.nav-link svg{width:12px;height:12px;fill:#3a8fd6}

/* tiles */
.column{position:absolute;width:235px;display:flex;flex-direction:column;gap:21px}
.tile{background:var(--card-bg);border-top:4px solid #f4f4f4;box-shadow:0 1px 3px rgba(0,0,0,.22)}
.tile-body{padding:10px 14px 0}
.store-name{font-size:9px;color:var(--text-dark);line-height:14px}
.tile-title{font-size:17.5px;font-weight:400;color:var(--link-blue);line-height:21px;margin-top:3px}
.tile-photo{width:206px;height:138px;margin-top:7px}
.price{font-size:21px;color:#3b3b3b;padding:6px 0 9px}
.counters{background:var(--band-bg);border-top:1px solid var(--line);border-bottom:1px solid var(--line);height:30px;display:flex;align-items:center;gap:14px;padding:0 14px;font-size:9px;color:var(--text-dark)}
.counters b{font-weight:400;color:var(--link-blue)}
.comment-form{display:flex;gap:12px;padding:9px 14px 8px}
.avatar{width:50px;height:50px;flex:none}
.comment-box{width:150px;height:69px;border:1px solid #dedede;padding:7px 10px;font-size:12px;font-style:italic;color:var(--placeholder);position:relative}
.comment-box::before{content:"";position:absolute;left:-7px;top:10px;width:12px;height:12px;background:#fff;border-left:1px solid #dedede;border-bottom:1px solid #dedede;transform:rotate(45deg)}
.comment{display:flex;gap:12px;padding:14px 14px 18px;border-top:1px solid var(--line);background:#fafafa}
.comment-author{font-size:11px;color:var(--link-blue);margin-bottom:3px}
.comment-text{font-family:Arial,sans-serif;font-size:11px;line-height:14px;color:var(--text-body)}

/* filter bar */
.filter-bar{position:absolute;left:0;top:842px;width:1200px;height:58px;background:var(--bar-bg);border-top:1px solid #c8c8c8}
.search{position:absolute;left:228px;top:11px;width:240px;height:34px;border-radius:17px;background:#f3f3f3;border:1px solid #bdbdbd;display:flex;align-items:center;gap:9px;padding-left:10px;font-size:13px;color:#8a8a8a}
.divider{position:absolute;top:0;width:1px;height:58px;background:#c4c4c4}
.filter{position:absolute;top:19px;font-size:13px;color:#3c3c3c;display:flex;align-items:center;gap:14px}
</style>
</head>
<body>

<header class="site-header">
  <div class="brand-mascot" role="img" aria-label="Brand mascot illustration"></div>
  <div class="brand-name">zAntelope</div>
  <div class="tagline">LOCAL PRODUCT SEARCH &amp; DISCOVERY</div>
  <span class="social" style="left:935px"></span>
  <span class="social" style="left:966px"></span>
</header>

<nav class="main-nav">
  <span class="nav-link" style="left:285px"><svg viewBox="0 0 12 12"><circle cx="6" cy="3.5" r="3"/><path d="M1 12c0-4 2-5.5 5-5.5s5 1.5 5 5.5z"/></svg>My Profile (Mark Ellison)</span>
  <span class="nav-link" style="left:503px"><svg viewBox="0 0 12 12"><path d="M0 1h6l6 6-5 5-7-6z"/></svg>My Products</span>
  <span class="nav-link" style="left:637px"><svg viewBox="0 0 12 12"><path d="M4.5 0h3v4.5H12v3H7.5V12h-3V7.5H0v-3h4.5z"/></svg>Add Products</span>
  <span class="nav-link" style="left:781px"><svg viewBox="0 0 12 12"><circle cx="4.5" cy="4.5" r="3.3" fill="none" stroke="#3a8fd6" stroke-width="2"/><path d="M7 7.5l1-1 4 4-1 1z"/></svg>Preview Store</span>
  <span class="nav-link" style="left:923px"><svg viewBox="0 0 12 12"><circle cx="7" cy="1.5" r="1.5"/><path d="M5 4h3l1 3 2 1-.5 1-3-1.5-1 2 2 3H7L5 9 3 12H2l2-5V5L2 6.5 1.5 6z"/></svg>Logout</span>
</nav>

<main>
  <div class="column" style="left:100px;top:138px">
    <article class="tile">
      <div class="tile-body">
        <div class="store-name">Plainform</div>
        <h2 class="tile-title">Sweet Sunflower Candle</h2>
        <div class="tile-photo" role="img" aria-label="Photo of a sunflower candle in a glass jar with its box" style="background:linear-gradient(135deg,#7a6f62,#b9b0a2 50%,#5f574c)"></div>
        <div class="price">$30</div>
      </div>
      <div class="counters"><span><b>2,520</b> Likes</span><span><b>146</b> Comments</span><span><b>55,435</b> Pods</span></div>
      <div class="comment-form"><div class="avatar" role="img" aria-label="User profile photo" style="background:#8c8c8c"></div><div class="comment-box">Leave comment here...</div></div>
    </article>
    <article class="tile">
      <div class="tile-body">
        <div class="store-name">Plainform</div>
        <h2 class="tile-title">Glass Centerpiece Vases</h2>
        <div class="tile-photo" role="img" aria-label="Photo of clear glass vases on a shelf" style="background:linear-gradient(135deg,#6f6f6f,#c8c8c8 50%,#555)"></div>
        <div class="price">$95</div>
      </div>
      <div class="counters"><span><b>2,520</b> Likes</span><span><b>146</b> Comments</span><span><b>55,435</b> Pods</span></div>
      <div class="comment-form"><div class="avatar" role="img" aria-label="User profile photo" style="background:#8c8c8c"></div><div class="comment-box">Leave comment here...</div></div>
    </article>
  </div>

  <div class="column" style="left:354px;top:138px">
    <article class="tile">
      <div class="tile-body">
        <div class="store-name">Plainform</div>
        <h2 class="tile-title">Parrot Crockscrew</h2>
        <div class="tile-photo" role="img" aria-label="Photo of a parrot-shaped corkscrew" style="background:linear-gradient(135deg,#a9a5a2,#c9c6c3)"></div>
        <div class="price">$62</div>
      </div>
      <div class="counters"><span><b>106</b> Likes</span><span><b>50</b> Comments</span><span><b>145</b> Pods</span></div>
      <div class="comment-form"><div class="avatar" role="img" aria-label="User profile photo" style="background:#8c8c8c"></div><div class="comment-box">Leave comment here...</div></div>
      <div class="comment"><div class="avatar" role="img" aria-label="Commenter profile photo" style="background:#6b5a66"></div><div><div class="comment-author">Tara Nolan</div><p class="comment-text">Nemo enim ipsam voluptatem quia voluptas sit aspernatur aut odit aut fugit, sed quia consequuntur magni dolores eos qui ratione voluptatem.</p></div></div>
    </article>
    <article class="tile">
      <div class="tile-body">
        <div class="store-name">Maison Lune</div>
        <h2 class="tile-title">Romantic Print Nightgown</h2>
        <div class="tile-photo" role="img" aria-label="Photo of a model wearing a floral print nightgown" style="background:linear-gradient(135deg,#e8e2dc,#b89a86 50%,#eee9e4)"></div>
      </div>
    </article>
  </div>

  <div class="column" style="left:610px;top:138px">
    <article class="tile">
      <div class="tile-body">
        <div class="store-name">Plainform</div>
        <h2 class="tile-title">Emergency Chocolate Rations</h2>
        <div class="tile-photo" role="img" aria-label="Photo of a tray of boxed chocolate bars" style="background:linear-gradient(135deg,#9a1c2a,#d2404f 50%,#c8487e)"></div>
        <div class="price">$5</div>
      </div>
      <div class="counters"><span><b>106</b> Likes</span><span><b>50</b> Comments</span><span><b>145</b> Pods</span></div>
      <div class="comment-form"><div class="avatar" role="img" aria-label="User profile photo" style="background:#8c8c8c"></div><div class="comment-box">Leave comment here...</div></div>
      <div class="comment"><div class="avatar" role="img" aria-label="Commenter avatar illustration" style="background:#c9d9e4"></div><div><div class="comment-author">Benji Cole</div><p class="comment-text">Nemo enim ipsam voluptatem quia voluptas sit aspernatur aut odit aut fugit.</p></div></div>
    </article>
    <article class="tile">
      <div class="tile-body">
        <div class="store-name">Plainform</div>
        <h2 class="tile-title">Pleated Fleece Scarf</h2>
        <div class="tile-photo" role="img" aria-label="Photo of a plum fleece hat and scarf on a display head" style="background:linear-gradient(135deg,#8a8580,#5e3a48 50%,#a6a19b)"></div>
        <div class="price">$60</div>
      </div>
    </article>
  </div>

  <div class="column" style="left:864px;top:138px">
    <article class="tile">
      <div class="tile-body">
        <div class="store-name">Plainform</div>
        <h2 class="tile-title">Isulated Beverage Holders</h2>
        <div class="tile-photo" role="img" aria-label="Photo of four patterned insulated cups with colored lids" style="background:linear-gradient(135deg,#6b6b6b,#d8d8d8 50%,#3a3a3a)"></div>
        <div class="price">$15</div>
      </div>
      <div class="counters"><span><b>106</b> Likes</span><span><b>50</b> Comments</span><span><b>145</b> Pods</span></div>
      <div class="comment-form"><div class="avatar" role="img" aria-label="User profile photo" style="background:#8c8c8c"></div><div class="comment-box">Leave comment here...</div></div>
      <div class="comment"><div class="avatar" role="img" aria-label="Commenter avatar illustration" style="background:#c9d9e4"></div><div><div class="comment-author">Benji Cole</div><p class="comment-text">Nemo enim ipsam voluptatem quia voluptas sit aspernatur aut odit aut fugit.</p></div></div>
    </article>
    <article class="tile">
      <div class="tile-body">
        <div class="store-name">Maison Lune</div>
        <h2 class="tile-title">Pleated Fleece Scarf</h2>
        <div class="tile-photo" role="img" aria-label="Photo of a model wearing a white lace top" style="background:linear-gradient(135deg,#c23a5c,#e9d7cf 55%,#d8576f)"></div>
      </div>
    </article>
  </div>
</main>

<div class="filter-bar">
  <div class="search"><svg width="16" height="16" viewBox="0 0 16 16"><circle cx="6.5" cy="6.5" r="5" fill="none" stroke="#777" stroke-width="2"/><path d="M10 10l5 5" stroke="#777" stroke-width="2.4"/></svg>Search...</div>
  <span class="divider" style="left:514px"></span>
  <span class="filter" style="left:538px">All Locations <svg width="6" height="10" viewBox="0 0 6 10"><path d="M0 4l3-4 3 4zM0 6l3 4 3-4z" fill="#444"/></svg></span>
  <span class="divider" style="left:654px"></span>
  <span class="filter" style="left:677px">All Price <svg width="6" height="10" viewBox="0 0 6 10"><path d="M0 4l3-4 3 4zM0 6l3 4 3-4z" fill="#444"/></svg></span>
  <span class="divider" style="left:770px"></span>
  <span class="filter" style="left:799px">All Retail Categories <svg width="6" height="10" viewBox="0 0 6 10"><path d="M0 4l3-4 3 4zM0 6l3 4 3-4z" fill="#444"/></svg></span>
  <span class="divider" style="left:968px"></span>
</div>

</body>
</html>
```